stationary
envelopes, letterhead, biz card
I need single sided standard sized Business Card [3.5" x 2"]
doesnt matter whatever looks good
Professional
Marten Olufsson
President
4218 Wexhollow Ave Ste 202-517
marten@bexlin.com
www.bexlin.com

```html
<!DOCTYPE html>
<html lang="en">
<head>
<meta charset="utf-8">
<title>Bexlin Stationery Set</title>
<link href="https://fonts.googleapis.com/css2?family=Open+Sans:wght@400;600;700&display=swap" rel="stylesheet">
<style>
  :root {
    --backdrop: #e6e8eb;
    --paper: #ffffff;
    --sky: #2aa9e0;
    --sky-deep: #1f8fc4;
    --navy: #1b3a5c;
    --ink: #141414;
    --muted: #6d7782;
    --ghost: #d9e9f3;
  }
  * { margin: 0; padding: 0; box-sizing: border-box; }
  html, body { width: 1200px; height: 580px; overflow: hidden; }
  body {
    background: var(--backdrop);
    font-family: "Open Sans", Arial, sans-serif;
    position: relative;
  }
  .sheet {
    position: absolute;
    background: var(--paper);
    box-shadow: 0 2px 8px rgba(0,0,0,.18);
    overflow: hidden;
  }
  .sheet svg.art { position: absolute; inset: 0; width: 100%; height: 100%; }

  .brand {
    position: absolute;
    display: flex;
    align-items: center;
    gap: 6px;
    font-weight: 700;
    color: var(--navy);
    letter-spacing: .5px;
    line-height: 1;
  }
  .brand-mark { background: var(--sky); display: block; }
  .ghost-name {
    position: absolute;
    font-weight: 700;
    color: var(--ghost);
    line-height: 1;
    letter-spacing: 2px;
  }

  /* Business card */
  .business-card { left: 91px; top: 190px; width: 150px; height: 90px; }
  .business-card .brand { left: 10px; top: 26px; font-size: 13px; gap: 4px; }
  .business-card .brand-mark { width: 8px; height: 8px; }
  .card-person {
    position: absolute; right: 8px; top: 8px;
    text-align: right; color: var(--paper);
    font-size: 5px; line-height: 1.35;
  }
  .card-person .name { font-weight: 700; font-size: 5.5px; }
  .card-contact {
    position: absolute; left: 10px; bottom: 9px;
    font-size: 4px; line-height: 1.45; color: var(--muted);
  }

  /* Letterhead */
  .letterhead { left: 288px; top: 29px; width: 380px; height: 523px; }
  .letterhead .brand { left: 30px; top: 136px; font-size: 22px; gap: 7px; }
  .letterhead .brand-mark { width: 13px; height: 13px; }
  .letterhead-contact {
    position: absolute; top: 14px; right: 14px;
    display: flex; gap: 16px;
    font-size: 5px; line-height: 1.5; color: var(--paper);
  }
  .letterhead .ghost-name { left: 80px; top: 250px; font-size: 54px; }

  /* Envelope */
  .envelope { left: 720px; top: 168px; width: 403px; height: 211px; }
  .envelope .brand { left: 48px; top: 46px; font-size: 16px; gap: 5px; }
  .envelope .brand-mark { width: 10px; height: 10px; }
  .envelope-return {
    position: absolute; left: 48px; top: 72px;
    font-size: 4.5px; line-height: 1.5; color: var(--muted);
  }
  .envelope .ghost-name { left: 228px; top: 82px; font-size: 34px; }
</style>
</head>
<body>

  <section class="sheet business-card" aria-label="Business card">
    <svg class="art" viewBox="0 0 150 90" preserveAspectRatio="none" aria-hidden="true">
      <path d="M40 0 H150 V34 C120 22 80 12 40 0 Z" fill="var(--sky)"/>
      <path d="M20 2 C70 12 115 24 150 40" fill="none" stroke="var(--ink)" stroke-width="1.4"/>
    </svg>
    <div class="brand"><span class="brand-mark"></span>Bexlin</div>
    <div class="card-person">
      <div class="name">Marten Olufsson</div>
      <div>President</div>
    </div>
    <div class="card-contact">
      <div>4218 Wexhollow Ave Ste 202-517</div>
      <div>marten@bexlin.com</div>
      <div>www.bexlin.com · 555-014-2290</div>
    </div>
  </section>

  <section class="sheet letterhead" aria-label="Letterhead">
    <svg class="art" viewBox="0 0 380 523" preserveAspectRatio="none" aria-hidden="true">
      <rect x="0" y="0" width="380" height="4" fill="var(--sky-deep)"/>
      <path d="M0 0 H380 V96 C290 60 160 32 0 22 Z" fill="var(--sky)"/>
      <path d="M0 42 C150 44 290 72 380 114" fill="none" stroke="var(--ink)" stroke-width="3"/>
    </svg>
    <div class="letterhead-contact">
      <div>
        <div>4218 Wexhollow Ave Ste 202-517</div>
        <div>Lakeview, TX 78230</div>
      </div>
      <div>
        <div>Phone 555-014-2290</div>
        <div>Fax 555-014-2291</div>
        <div>marten@bexlin.com</div>
        <div>www.bexlin.com</div>
      </div>
    </div>
    <div class="brand"><span class="brand-mark"></span>Bexlin</div>
    <div class="ghost-name" aria-hidden="true">Bexlin</div>
  </section>

  <section class="sheet envelope" aria-label="Envelope">
    <div class="brand"><span class="brand-mark"></span>Bexlin</div>
    <div class="envelope-return">
      <div>4218 Wexhollow Ave Ste 202-517</div>
      <div>Lakeview, TX 78230</div>
    </div>
    <div class="ghost-name" aria-hidden="true">Bexlin</div>
  </section>

</body>
</html>
```